Bordkarte MY Frelk
Unsere Ideen wurden sehr gut aufgenommen und in der Diskussion weiterentwickelt. Wir freuen uns, das Design einsetzen zu können
Zielgruppe
Bordkarte für ein Rentnerpaar, welches nahezu ganzjährig auf dem eigenen Motorschiff Nord- und Ostsee bereist.
Bei einer Bordkarte stehen Angaben zum Motorschiff im Fokus (Funkkennzeichen Identifikationsnummer)und nicht die des Eignerpaars das maximal mit Vornamen erscheint.
Die Karte wird anderen Eignern abgegeben und dient dazu, dass man sich auch auf grosse Distanzen suchen und kontaktieren kann. So wird bei diesen meist Einzelgängern das soziale Umfeld gepflegt.
Für nicht Berner, 'Frelk' ist Dialekt und bedeutet 'Bär'
Aufgabenstellung
Originelles*, maritimes Sujet oder markantes, nördliches Sternzeichen
(*keine Anker oder Muscheln!)
Maritimes Design, zurückhaltend, repräsentativ.
Die Karte soll das Gefühl der Ruhe und Zufriedenheit vermitteln
Schiff und Namesdesign als Bilder im Anhang. Die Rechte für das Wappen, habe ich einmalig für den Namen erworben.
MY Frelk
Henrike & Olaf
MMSI: 471.803.915
CS: KQRT7
InmarSat : 004926 81037

```html
<!DOCTYPE html>
<html lang="de">
<head>
<meta charset="UTF-8">
<title>Bordkarte MY Frelk</title>
<link rel="stylesheet" href="https://fonts.googleapis.com/css2?family=Kumbh+Sans:wght@700;800&display=swap">
<style>
  :root {
    --page-bg: #f2f2f0;
    --card-paper: #fbfaf7;
    --sea-blue: #2b8ec6;
    --white: #ffffff;
    --tower-red: #b54d45;
    --rock-dark: #363a4c;
    --initials-tint: #4ea3d3;
  }
  * { margin: 0; padding: 0; box-sizing: border-box; }
  html, body {
    width: 1200px;
    height: 1200px;
    overflow: hidden;
    background: var(--page-bg);
  }
  .boarding-card {
    position: absolute;
    left: 100px;
    top: 277px;
    width: 1000px;
    height: 646px;
    background: var(--card-paper);
    overflow: hidden;
    font-family: "Kumbh Sans", sans-serif;
  }
  .rule {
    position: absolute;
    top: 168px;
    height: 10px;
    width: 380px;
    background: var(--sea-blue);
  }
  .rule--left { left: 0; }
  .rule--right { right: 0; }
  .name-block {
    position: absolute;
    left: 432px;
    top: 98px;
    width: 136px;
    height: 136px;
    background: var(--sea-blue);
    display: flex;
    align-items: center;
    justify-content: center;
    text-align: center;
  }
  .name-block__text {
    color: var(--white);
    font-weight: 800;
    font-size: 30px;
    line-height: 1;
    letter-spacing: 0.5px;
    text-transform: uppercase;
  }
  .vessel-ids {
    position: absolute;
    left: 0;
    top: 294px;
    width: 1000px;
    text-align: center;
    color: var(--sea-blue);
    font-weight: 700;
    font-size: 30px;
    line-height: 44px;
    list-style: none;
  }
  .sea-band {
    position: absolute;
    left: 0;
    bottom: 0;
    width: 1000px;
    height: 178px;
    background: var(--sea-blue);
  }
  .owner-initials {
    position: absolute;
    left: 84px;
    top: 536px;
    width: 106px;
    height: 64px;
  }
  .lighthouse {
    position: absolute;
    left: 694px;
    top: 180px;
    width: 306px;
    height: 466px;
  }
</style>
</head>
<body>
  <main class="boarding-card">
    <div class="rule rule--left"></div>
    <div class="rule rule--right"></div>

    <div class="name-block">
      <span class="name-block__text">MY<br>Frelk</span>
    </div>

    <ul class="vessel-ids">
      <li>MMSI: 471.803.915</li>
      <li>CS: KQRT7</li>
      <li>InmarSat: 004926 81037</li>
    </ul>

    <div class="sea-band"></div>

    <svg class="owner-initials" viewBox="0 0 106 64" role="img" aria-label="Handgeschriebene Initialen H&amp;O des Eignerpaars">
      <rect width="106" height="64" rx="8" fill="var(--initials-tint)"/>
    </svg>

    <svg class="lighthouse" viewBox="0 0 306 466" role="img" aria-label="Illustration: roter Leuchtturm auf dunklem Felsen im Meer">
      <defs>
        <linearGradient id="lighthouse-tone" x1="0" y1="0" x2="0" y2="1">
          <stop offset="0" stop-color="var(--tower-red)"/>
          <stop offset="0.7" stop-color="var(--tower-red)"/>
          <stop offset="1" stop-color="var(--rock-dark)"/>
        </linearGradient>
      </defs>
      <rect x="0" y="0" width="306" height="466" rx="14" fill="url(#lighthouse-tone)"/>
    </svg>
  </main>
</body>
</html>
```